Metal Recycling Website Require New Design for upgrade

Our company currently have an existing website, www.tavorinmetal.com and the website is generally outdated so we would like an improvement.

We would generally prefer to keep the current color theme of our website as it is similar to our current logo.

We would also like our company factory picture to be on somewhere of the webpage (but only if the designer think that the picture can blend well with the color theme)

Our company is dealing alot Aluminiun, Stainless Steel, Copper, Brass, Iron

Pictures uploaded.

Target Market(s)

General Commercial Manufacturer, B2B

Industry/Entity Type

Recycling

Number of Pages Required

1 page

Colors

Designer to choose colors to be used in the design.

Requirements
Must have
• Hopefully color will be similar to my logo theme but designer welcome to have their own input.
Nice to have
• Company Picture (Uploaded in the file)

```html
<!DOCTYPE html>
<html lang="en">
<head>
<meta charset="utf-8">
<title>Tavorin Metal Recycling</title>
<link rel="stylesheet" href="https://fonts.googleapis.com/css2?family=Montserrat:wght@700&family=Roboto:wght@300;400;500;700&display=swap">
<style>
:root{
  --gold:#dbae38;
  --dark:#4a4646;
  --darker:#3f3b3b;
  --sand:#ebe9e6;
  --ink:#4a4646;
  --white:#ffffff;
}
*{box-sizing:border-box;margin:0;padding:0}
html,body{width:694px;height:1200px;overflow:hidden;background:var(--white)}
body{font-family:'Roboto',sans-serif;color:var(--ink)}
.page{position:relative;width:694px;height:1200px;overflow:hidden;background:var(--white)}
.abs{position:absolute}
.shapes{position:absolute;left:0;top:0}

/* header */
.brand{left:51px;top:26px;display:flex;align-items:center;gap:4px;color:var(--gold);font-weight:500;font-size:8.5px;letter-spacing:.5px}
.brand-mark{width:14px;height:14px;border:1.5px solid var(--gold)}
.nav a{position:absolute;top:31px;font-size:8px;color:var(--ink);text-decoration:none;letter-spacing:.1px}
.nav a.active{color:var(--gold)}
.nav a.active::after{content:"";position:absolute;left:0;top:10px;width:11px;height:1px;background:var(--gold)}

/* hero */
.hero-title{left:76px;top:139px;font-family:'Montserrat',sans-serif;font-weight:700;font-size:36px;letter-spacing:-1.5px;color:var(--dark);line-height:1}
.hero-sub{left:77px;top:173px;font-family:'Montserrat',sans-serif;font-weight:700;font-size:24px;color:var(--gold);letter-spacing:.3px;line-height:1}
.hero-text{left:77px;top:216px;width:230px;font-size:8.4px;line-height:10.5px;color:#5a5656}
.btn{display:flex;align-items:center;justify-content:center;background:var(--gold);color:var(--white);font-weight:700;font-size:8px;box-shadow:0 1px 3px rgba(0,0,0,.2)}
.hero-btn{left:77px;top:252px;width:87px;height:22px}

/* headings */
.heading{font-weight:500;color:var(--ink);position:absolute}
.heading::after{content:"";position:absolute;left:0;bottom:-2px;width:16px;height:1.2px;background:var(--gold)}
.section-title{font-size:13.5px;font-weight:500}
.small-title{font-size:8.4px;font-weight:500}
.small-title::after{width:8px;bottom:-2px}

/* about */
.about{left:0;top:391px;width:694px;height:218px;background:var(--sand)}
.about-copy{left:146px;width:402px;text-align:center;font-weight:300;font-size:8.6px;line-height:10.5px;color:#3a3737}

/* search */
.search{height:20px;width:191px;border:1px solid var(--gold);background:var(--white);display:flex;align-items:center;justify-content:space-between;padding:0 6px;font-size:7px;font-style:italic;font-weight:300;color:#777}
.card-img{width:141px;height:63px}
.card-cap{position:absolute;left:0;bottom:0;width:100%;height:16px;background:rgba(40,38,38,.6);color:var(--white);font-size:7.2px;display:flex;align-items:center;justify-content:center}
.read-more{font-size:7px;font-style:italic;font-weight:300;color:#666;text-align:right;width:141px}
.read-more span{border-bottom:1px solid var(--gold)}

/* contact */
.contact-band{left:0;top:835px;width:694px;height:220px;background:var(--sand)}
.cta-big{left:121px;top:902px;font-weight:700;font-size:33px;color:var(--gold);letter-spacing:-.3px;line-height:1}
.cta-mid{left:122px;top:936px;font-weight:700;font-size:21px;color:var(--dark);line-height:1}
.cta-rule{left:122px;top:961px;width:28px;height:2px;background:var(--gold)}
.field{width:167px;height:20px;border:1px solid var(--gold);background:#faf9f8}
.submit{left:526px;top:1013px;width:46px;height:20px;font-size:8px}

/* footer */
.footer{left:0;top:1055px;width:694px;height:126px;background:var(--dark)}
.footer-bar{left:0;top:1181px;width:694px;height:19px;background:var(--darker)}
.footer .heading,.foot-head{color:var(--white)}
.foot-text{font-size:7.2px;line-height:10.5px;color:#ece9e4;font-weight:300}
.foot-nav{font-size:7.2px;color:#ece9e4;font-weight:300}
.social{width:12px;height:12px;border-radius:2px;background:#e2dfdb}
.copyright{left:0;top:1187px;width:694px;text-align:center;font-size:7px;color:#e8e6e2;font-weight:400}
</style>
</head>
<body>
<div class="page">

  <!-- background bands -->
  <div class="abs about"></div>
  <div class="abs contact-band"></div>
  <div class="abs footer"></div>
  <div class="abs footer-bar"></div>

  <svg class="shapes" width="694" height="1200" viewBox="0 0 694 1200" aria-hidden="true">
    <polygon points="581,0 694,0 694,112" fill="#4a4646"/>
    <polygon points="0,279 112,391 0,503" fill="#4a4646"/>
    <polygon points="694,224 521,391 694,564" fill="#dbae38"/>
    <polygon points="0,757 79,835 0,914" fill="#dbae38"/>
    <polygon points="694,1064 556,1200 694,1200" fill="#dbae38"/>
  </svg>

  <!-- header -->
  <div class="abs brand"><span class="brand-mark"></span><span>TAVORIN METAL</span></div>
  <nav class="nav">
    <a class="active" style="left:204px" href="#">HOME</a>
    <a style="left:256px" href="#">ABOUT US</a>
    <a style="left:321px" href="#">PRODUCT</a>
    <a style="left:384px" href="#">OUR SERVICE</a>
    <a style="left:458px" href="#">CONTACT</a>
  </nav>

  <!-- hero -->
  <div class="abs hero-title">RECYCLE</div>
  <div class="abs hero-sub">IT'S YOUR FUTURE</div>
  <p class="abs hero-text">We cannot solve our problems with the same thinking we used when we created them</p>
  <div class="abs btn hero-btn">I HAVE SCRAP</div>

  <svg class="shapes" width="694" height="1200" viewBox="0 0 694 1200">
    <defs>
      <linearGradient id="gWorker" x1="0" y1="0" x2="1" y2="1"><stop offset="0" stop-color="#c9a23a"/><stop offset="1" stop-color="#4d5f7a"/></linearGradient>
      <linearGradient id="gFactory" x1="0" y1="0" x2="1" y2="1"><stop offset="0" stop-color="#3e6fd1"/><stop offset="1" stop-color="#7fb59e"/></linearGradient>
      <linearGradient id="gYard" x1="0" y1="0" x2="1" y2="1"><stop offset="0" stop-color="#3f78d4"/><stop offset="1" stop-color="#8a8884"/></linearGradient>
      <linearGradient id="gFoil" x1="0" y1="0" x2="1" y2="1"><stop offset="0" stop-color="#9a9b9e"/><stop offset="1" stop-color="#3d3e42"/></linearGradient>
      <filter id="soft" x="-20%" y="-20%" width="140%" height="140%"><feDropShadow dx="0" dy="4" stdDeviation="5" flood-opacity=".25"/></filter>
    </defs>
    <g filter="url(#soft)">
      <polygon role="img" aria-label="Worker sorting scrap metal" points="511,88 558,135 511,182 464,135" fill="url(#gWorker)"/>
      <polygon role="img" aria-label="Company factory building" points="460,139 507,186 460,233 413,186" fill="url(#gFactory)"/>
      <polygon role="img" aria-label="Excavator over scrap yard" points="562,139 609,186 562,233 515,186" fill="url(#gYard)"/>
      <polygon role="img" aria-label="Crushed aluminium scrap" points="511,190 558,237 511,284 464,237" fill="url(#gFoil)"/>
    </g>
  </svg>

  <!-- about -->
  <h2 class="heading section-title" style="left:316px;top:405px">ABOUT US</h2>
  <p class="abs about-copy" style="top:435px">Tavorin Metal Recycling is a privately-held company located in Singapore with a humble beginning. We has grown rapidly through the continuous support of our customer and suppliers and currently have supplier across various industries including, general public, constructions, manufacturers, engineering, demolition, shipyards, other recycling yards and overseas customer.</p>
  <p class="abs about-copy" style="top:498px">Tavorin Metal Recycling has become a recycling industry leader in the local market, committed to responsibly and efficiently serving all its customer, supplier and community with integrity and professionalism, and in an environmentally safe manner.</p>
  <p class="abs about-copy" style="top:551px">We are committed to our suppliers and consumers by effectively sourcing, processing, and marketing scrap metal for recycling. We actively pursue new and long lasting relationships by partnering with our customers, providing quality service built upon integrity, honesty, and professionalism. We are committed to meeting all our customers needs by exceeding their expectations.</p>

  <!-- search -->
  <h2 class="heading section-title" style="left:263px;top:627px">SEARCH FOR OUR PRODUCT</h2>
  <h3 class="heading small-title" style="left:122px;top:657px">Search by Material</h3>
  <h3 class="heading small-title" style="left:381px;top:657px">Search by Product</h3>
  <div class="abs search" style="left:122px;top:675px"><span>Search</span>
    <svg width="11" height="11" viewBox="0 0 11 11"><circle cx="5" cy="5" r="4" fill="none" stroke="#666" stroke-width="1"/><line x1="8" y1="8" x2="10.5" y2="10.5" stroke="#666" stroke-width="1"/></svg></div>
  <div class="abs search" style="left:381px;top:675px"><span>Search</span>
    <svg width="11" height="11" viewBox="0 0 11 11"><circle cx="5" cy="5" r="4" fill="none" stroke="#666" stroke-width="1"/><line x1="8" y1="8" x2="10.5" y2="10.5" stroke="#666" stroke-width="1"/></svg></div>

  <h3 class="heading small-title" style="left:122px;top:723px">FOR INDIVIDUAL</h3>
  <h3 class="heading small-title" style="left:276px;top:723px">FOR CORPORATE</h3>
  <h3 class="heading small-title" style="left:431px;top:723px">FOR INTERNATIONAL</h3>

  <div class="abs card-img" role="img" aria-label="Pile of dark sheet metal scrap" style="left:122px;top:739px;background:linear-gradient(135deg,#6f6c72,#2a2829)"><div class="card-cap">Do Your Part, Recycle With Us Today</div></div>
  <div class="abs card-img" role="img" aria-label="Bundled aluminium profile scrap" style="left:276px;top:739px;background:linear-gradient(135deg,#5f6f94,#b9c2d6 50%,#3b4156)"><div class="card-cap">Get The Best Value For Your Scrap</div></div>
  <div class="abs card-img" role="img" aria-label="Shredded stainless steel scrap" style="left:431px;top:739px;background:linear-gradient(135deg,#c7c9cc,#6c6e72 60%,#3a3b3e)"><div class="card-cap">Your Trusted Global Partner</div></div>

  <div class="abs read-more" style="left:122px;top:807px"><span>Read</span> More &gt;</div>
  <div class="abs read-more" style="left:276px;top:807px"><span>Read</span> More &gt;</div>
  <div class="abs read-more" style="left:431px;top:807px"><span>Read</span> More &gt;</div>

  <!-- contact -->
  <div class="abs cta-big">HAVE SCRAP?</div>
  <div class="abs cta-mid">GET US CONTACT YOU</div>
  <div class="abs cta-rule"></div>

  <h3 class="heading small-title" style="left:405px;top:878px">Name</h3>
  <div class="abs field" style="left:405px;top:895px"></div>
  <h3 class="heading small-title" style="left:405px;top:923px">Email</h3>
  <div class="abs field" style="left:405px;top:940px"></div>
  <h3 class="heading small-title" style="left:405px;top:969px">Contact</h3>
  <div class="abs field" style="left:405px;top:985px"></div>
  <div class="abs btn submit">SUBMIT</div>

  <!-- footer -->
  <h3 class="heading small-title foot-head" style="left:116px;top:1073px;color:#fff">CERTIFICATE</h3>
  <div class="abs" style="left:116px;top:1091px;width:124px;height:52px;background:#fff;padding:3px">
    <div role="img" aria-label="Certification badges" style="width:100%;height:100%;border:1px solid #4aa9d6;display:flex;align-items:center;gap:6px;padding:4px">
      <div style="width:24px;height:24px;border-radius:50%;background:#1aa3d9"></div>
      <div style="width:38px;height:34px;border:1px solid #4aa9d6"></div>
      <div style="width:26px;height:34px;background:#1f3e8c"></div>
    </div>
  </div>

  <h3 class="heading small-title" style="left:319px;top:1073px;color:#fff">CONTACT US</h3>
  <div class="abs foot-text" style="left:319px;top:1090px">18 Harrow Industrial Lane, Singapore 700118<br>+65-90001234<br>sales@tavorinmetal.com</div>
  <h3 class="heading small-title" style="left:318px;top:1133px;color:#fff">WE ARE ON SOCIAL MEDIA</h3>
  <div class="abs social" role="img" aria-label="Social network link" style="left:319px;top:1151px"></div>
  <div class="abs social" role="img" aria-label="Social network link" style="left:340px;top:1151px"></div>
  <div class="abs social" role="img" aria-label="Social network link" style="left:362px;top:1151px"></div>
  <div class="abs social" role="img" aria-label="Social network link" style="left:384px;top:1151px"></div>

  <h3 class="heading small-title" style="left:528px;top:1073px;color:#fff">NAVIGATION</h3>
  <div class="abs foot-nav" style="left:528px;top:1091px">HOME</div>
  <div class="abs foot-nav" style="left:528px;top:1103px">ABOUT US</div>
  <div class="abs foot-nav" style="left:528px;top:1116px">PRODUCT</div>
  <div class="abs foot-nav" style="left:528px;top:1128px">OUR SERVICE</div>
  <div class="abs foot-nav" style="left:528px;top:1141px">CONTACT</div>

  <div class="abs copyright">COPYRIGHT : WEBOWNER. ALL RIGHTS RESERVED</div>
</div>
</body>
</html>
```